Software Platform User Guide (Manual)

We need a user manual template for our online e-learning platform, Lanterna, which allows users to create their own online courses.

We’re looking for a template for a few pages, including a cover, back page, table of contents, and pages for text-only (or bullet points), and text & images (screenshots). We would like to be able to add new pages and adjust textual content ourselves. Lorem ipsum is totally cool as placeholder text. The name of the product is Lanterna, but the company name is Coastal Meridian Works, so we would like the cover and back cover to say “Coastal Meridian Works" and "Lanterna".

We have uploaded a few files to give you a sense of our color scheme and logo. You can also check out our website at cmwvista.example for an idea of our aesthetic sensibility. The design should be simple and elegant, and (being a user manual) clarity is king. We use Avenir and Elizabeth as or primary fonts. We have also uploaded some sample screen shots from Lanterna. You can use those screenshots to help direct your work, but note that the interface design is changing soon; i.e., you should emphasize the Coastal Meridian Works brand aesthetic more so than the Lanterna user interface design.

Target Market(s)

Businesses and nonprofits looking to implement our platform. Many buyers are female, but the people reading the manual are typically male.

Industry/Entity Type

It Company

Requirements
Must have
• The final product must be a template that will work in Microsoft Word, PowerPoint, or Apple Keynote/Pages. It's fine to send PDFs for previews. Note we need the final product in ONE of the above choices (Word, Powerpoint, Keynote, or Pages), not ALL.

You must make use of the CMW logo and fonts on every page. Note that the tag line, "every quiet harbor holds a brighter tide" in one version of the logo does note have to be included.

We need clear delineation between headers, sub-headers, and bullets, as well as a great looking cover, table of contents and back page.

Please Note: Please disregard the OLVA logo on any screenshots. These were mockups for a client. Please don't use the OLVA name or logo.

```html
<!DOCTYPE html>
<html lang="en">
<head>
<meta charset="utf-8">
<title>Coastal Meridian Works — Lanterna User Guide Cover</title>
<link rel="stylesheet" href="https://fonts.googleapis.com/css2?family=Tinos:ital,wght@0,400;1,400&display=swap">
<style>
  :root {
    --navy: #213d5a;
    --lime: #b5cf32;
    --sky: #3b93d3;
    --dot: #4f8ccb;
    --ink: #4a4d52;
    --paper: #ffffff;
    --key-light: #eceef0;
    --key-shade: #cdd1d5;
    --page-bg: #f2f2f2;
  }
  html, body {
    margin: 0;
    padding: 0;
    width: 861px;
    height: 1200px;
    overflow: hidden;
    background: var(--page-bg);
  }
  .cover {
    display: block;
    width: 861px;
    height: 1200px;
    font-family: "Tinos", "Times New Roman", serif;
  }
  .cover__ground { fill: var(--navy); }
  .brand-mark__disc { fill: var(--lime); }
  .brand-mark__name { fill: var(--paper); font-size: 58px; font-weight: 400; letter-spacing: 1px; }
  .brand-title { fill: var(--lime); font-size: 37px; font-weight: 400; }
  .brand-tagline { fill: var(--paper); font-size: 16.5px; letter-spacing: 1.9px; }
  .hero__accent { fill: var(--lime); }
  .hero__key { fill: var(--sky); }
  .product-name { fill: var(--paper); font-size: 84px; letter-spacing: 3px; }
  .web-dot { fill: var(--dot); }
  .web-address { font-size: 22px; font-style: italic; letter-spacing: 5px; fill: var(--ink); }
  .web-address__domain { fill: var(--dot); }
</style>
</head>
<body>
<svg class="cover" viewBox="0 0 861 1200" xmlns="http://www.w3.org/2000/svg">
  <defs>
    <clipPath id="sheet"><rect width="861" height="1200"/></clipPath>
    <clipPath id="hero-window"><circle cx="562" cy="804" r="515"/></clipPath>
    <linearGradient id="hero-tone" x1="0" y1="0" x2="1" y2="1">
      <stop offset="0" stop-color="var(--key-light)"/>
      <stop offset="1" stop-color="var(--key-shade)"/>
    </linearGradient>
  </defs>

  <rect class="cover__ground" width="861" height="1200"/>

  <g class="brand-mark">
    <circle class="brand-mark__disc" cx="195" cy="178" r="96"/>
    <text class="brand-mark__name" x="195" y="198" text-anchor="middle">CMW</text>
  </g>

  <text class="brand-title" x="355" y="173">Coastal Meridian Works</text>
  <text class="brand-tagline" x="356" y="212">every quiet harbor holds a brighter tide</text>

  <g class="hero" clip-path="url(#sheet)">
    <circle class="hero__accent" cx="540" cy="806" r="517"/>
    <g clip-path="url(#hero-window)">
      <rect role="img" aria-label="Close-up photograph of a white computer keyboard" x="0" y="280" width="861" height="920" fill="url(#hero-tone)"/>
      <rect class="hero__key" x="-117" y="-275" width="234" height="550" rx="22" transform="translate(446 716) rotate(34)"/>
      <text class="product-name" text-anchor="middle" transform="translate(436 740) rotate(-56)">Lanterna</text>
    </g>
  </g>

  <circle class="web-dot" cx="141" cy="994" r="27"/>
  <text class="web-address" transform="translate(190 1020) rotate(28)">www.<tspan class="web-address__domain"> cmwvista</tspan>.example</text>
</svg>
</body>
</html>
```